Business Card for Language School (2 locations)

We need a sleek business card for a language school that is looking to update our image to be more professional. We work with students ages Pre-Kindergarten through adults. Our idea is to have an all-black business card with white or silver lettering. On the front will be the name of our school (Bright Maple English Academy), and on the back there will be information for our location, phone number, email, and website (and possibly social media information). We have two school branches, so the address, phone number, and email address will be different for each branch, but all of the other information will stay the same. We'd like each branch to have a different color card edge that is neon. We are also open to suggestions and new ideas!

Some answers to questions we have received:
1. The reason we haven't added a logo is because we are looking to get a new one. We hadn't originally planned to do that at this time, but we are going to look into updating our project to include that as another aspect of it. We had previously planned to just include the school name on the front without a logo at this time.
2. We currently have two branches of our school, and we want our business card design to be uniform for each location. While it might make sense to put the information on one card right now, we plan to have more locations in the future, so we want to plan ahead with a unified design right now.
3. Our school addresses and phone numbers can be found on our website: www.brightmapleenglish.example (at the bottom of the page)!
Updates

Part of this contest is also a new logo design. Our previous design was a train, which we would be open to keeping if it had an updated, sleeker design.

Contact Information for Business Card

Card #1:
Bright Maple English Academy (Qiaolin Branch)
Yuqing W. Rd. Sec. 3, Lane 412, No. 29, 1F
Beitou District, Taipei City 11268
02-2649-3058
qiaolin@brightmapleenglish.example

Card #2:
Bright Maple English Academy (Fenghe Branch)
Fulan Road, No. 318, 1F
Songshan District, Taipei City 10573
02-2761-4402
fenghe@brightmapleenglish.example

Both cards:
Website: www.brightmapleenglish.example
social page: www.facebook.com/brightmapleenglish
photo page: @brightmapleenglish

```html
<!DOCTYPE html>
<html lang="en">
<head>
<meta charset="utf-8">
<title>Bright Maple English Academy – Business Card</title>
<link rel="stylesheet" href="https://fonts.googleapis.com/css2?family=Fira+Sans:wght@600&family=Alegreya+Sans+SC:wght@400;500&display=swap">
<style>
  :root {
    --backdrop: #9a9a9a;
    --card-black: #03070f;
    --card-navy: #0b1a33;
    --sheen: #2c5590;
    --silver: #d9dde3;
    --ink: #b9c6dc;
    --icon-blue: #4a72ad;
    --edge-qiaolin: #e8b318;
    --edge-fenghe: #5fe3dc;
    --map-grey: #e4e4e4;
  }
  html, body { margin: 0; padding: 0; overflow: hidden; }
  body {
    width: 1200px; height: 1200px;
    background: radial-gradient(circle at 50% 55%, #e6e6e6 0%, var(--backdrop) 70%, #6f6f6f 100%);
    position: relative;
    font-family: "Alegreya Sans SC", sans-serif;
  }
  .card {
    position: absolute; left: 190px;
    width: 820px; height: 500px;
    border-radius: 30px;
    overflow: hidden;
    background:
      linear-gradient(90deg, transparent 30%, rgba(44,85,144,.55) 48%, rgba(44,85,144,.15) 56%, transparent 66%),
      linear-gradient(180deg, var(--card-navy) 0%, var(--card-black) 100%);
    box-shadow: 0 18px 40px rgba(0,0,0,.35);
  }
  .card-front { top: 60px; }
  .card-back { top: 620px; }
  .front-curves { position: absolute; inset: 0; }
  .school-name {
    position: absolute; left: 0; right: 0; top: 120px;
    margin: 0; text-align: center;
    font-family: "Fira Sans", sans-serif; font-weight: 600;
    font-size: 66px; line-height: 1.08; color: var(--silver);
    letter-spacing: .5px;
  }
  .website {
    position: absolute; left: 0; right: 0; top: 410px;
    text-align: center; font-size: 22px; letter-spacing: 2px; color: var(--ink);
  }
  .divider {
    position: absolute; left: 410px; top: 30px; width: 1px; height: 300px;
    background: linear-gradient(180deg, transparent, rgba(120,150,200,.35), transparent);
  }
  .branch-edge { position: absolute; width: 14px; }
  .edge-qiaolin { left: 46px; top: 36px; height: 142px; background: var(--edge-qiaolin); }
  .edge-fenghe { left: 752px; top: 76px; height: 142px; background: var(--edge-fenghe); }
  .map-area { position: absolute; background: linear-gradient(135deg, #f2f2f2, var(--map-grey)); }
  .map-qiaolin { left: 66px; top: 36px; width: 280px; height: 142px; }
  .map-fenghe { left: 478px; top: 76px; width: 268px; height: 142px; background: linear-gradient(180deg, #f2f2f2 55%, #bfe3b6 75%, #e9e9e9); }
  .branch-info {
    position: absolute; margin: 0; font-size: 15px; line-height: 1.3; color: var(--ink);
  }
  .info-qiaolin { left: 46px; top: 192px; width: 330px; }
  .info-fenghe { left: 478px; top: 232px; width: 290px; }
  .contact-line {
    position: absolute; display: flex; align-items: center; gap: 10px;
    font-size: 15px; color: var(--ink);
  }
  .contact-line svg { flex: none; fill: var(--icon-blue); }
  .phone-qiaolin { left: 46px; top: 300px; }
  .phone-fenghe { left: 478px; top: 296px; }
  .mail-admissions { left: 46px; top: 350px; line-height: 1.25; }
  .mail-director { left: 478px; top: 394px; line-height: 1.25; }
  .social { position: absolute; left: 46px; top: 404px; display: flex; gap: 10px; }
  .social span { width: 24px; height: 24px; border: 2px solid var(--icon-blue); border-radius: 5px; box-sizing: border-box; }
  .school-time {
    position: absolute; left: 110px; top: 404px; width: 360px;
    font-size: 17px; line-height: 1.3; color: var(--silver); letter-spacing: .5px;
  }
</style>
</head>
<body>

<section class="card card-front">
  <svg class="front-curves" viewBox="0 0 820 500" aria-hidden="true">
    <path d="M20 300 Q 420 360 810 170" fill="none" stroke="#4b78b8" stroke-width="2" opacity=".7"/>
    <path d="M40 390 Q 470 370 810 230" fill="none" stroke="#35598f" stroke-width="1.5" opacity=".6"/>
  </svg>
  <h1 class="school-name">Bright Maple<br>English Academy</h1>
  <div class="website">www.brightmapleenglish.example</div>
</section>

<section class="card card-back">
  <div class="divider"></div>

  <div class="branch-edge edge-qiaolin"></div>
  <div class="map-area map-qiaolin" role="img" aria-label="Street map of the Qiaolin Branch location"></div>
  <p class="branch-info info-qiaolin">Qiaolin: Yuqing W. Rd. Sec. 3, Lane 412, No. 29, 1F, Beitou District, Taipei City<br>Bus routes: 220, 279, 612, 902 (exit at the bus stop in front of Riverside International School or Qiaolin Sports Park)</p>
  <div class="contact-line phone-qiaolin">
    <svg width="18" height="18" viewBox="0 0 24 24" aria-hidden="true"><path d="M6.6 10.8a15 15 0 0 0 6.6 6.6l2.2-2.2c.3-.3.7-.4 1-.2 1.1.4 2.3.6 3.6.6.6 0 1 .4 1 1V20c0 .6-.4 1-1 1A17 17 0 0 1 3 4c0-.6.4-1 1-1h3.5c.6 0 1 .4 1 1 0 1.3.2 2.5.6 3.6.1.3 0 .7-.2 1z"/></svg>
    02-2649-3058
  </div>
  <div class="contact-line mail-admissions">
    <svg width="22" height="18" viewBox="0 0 24 20" aria-hidden="true"><path d="M2 8 12 1l10 7v10a1 1 0 0 1-1 1H3a1 1 0 0 1-1-1zM4 9l8 5 8-5-8-5z"/></svg>
    <span>For admissions:<br>admissions@brightmapleenglish.example</span>
  </div>
  <div class="social" aria-label="Social pages: brightmapleenglish"><span></span><span></span></div>
  <div class="school-time" style="left:116px;width:680px;top:410px">School Time: Monday – Friday 09:00 – 21:00, Saturday 09:00 – 18:00</div>

  <div class="branch-edge edge-fenghe"></div>
  <div class="map-area map-fenghe" role="img" aria-label="Street map of the Fenghe Branch location"></div>
  <p class="branch-info info-fenghe">Fenghe 1F, Fulan Road, No. 318,<br>Songshan District, Taipei City</p>
  <div class="contact-line phone-fenghe">
    <svg width="18" height="18" viewBox="0 0 24 24" aria-hidden="true"><path d="M6.6 10.8a15 15 0 0 0 6.6 6.6l2.2-2.2c.3-.3.7-.4 1-.2 1.1.4 2.3.6 3.6.6.6 0 1 .4 1 1V20c0 .6-.4 1-1 1A17 17 0 0 1 3 4c0-.6.4-1 1-1h3.5c.6 0 1 .4 1 1 0 1.3.2 2.5.6 3.6.1.3 0 .7-.2 1z"/></svg>
    02-2761-4402
  </div>
  <div class="contact-line mail-director" style="top:346px">
    <svg width="22" height="18" viewBox="0 0 24 20" aria-hidden="true"><path d="M2 8 12 1l10 7v10a1 1 0 0 1-1 1H3a1 1 0 0 1-1-1zM4 9l8 5 8-5-8-5z"/></svg>
    <span>For all other inquiries:<br>director@brightmapleenglish.example</span>
  </div>
</section>

</body>
</html>
```